Style Template created - Report Accounting and Advisory industry

We need a style template created to set out a report for advice. The report follows <br/><br/>- Cover Page - ( we would need to print to a letter head )<br/>- General Disclaimer<br/>- Space to add Excel Reports in to the document- Maybe inserted Pdf's later<br/>- Action Plan dot points under headings<br/>- List of Strategies to be adopted<br/><br/>Attached is a quick example word doc that needs Custom Style Templates made so that we can quickly format items added. Also the ugly PDF that we currently produce for clients <br/><br/>Red - is our preferred Colour<br/><br/>

Target Market(s)

Accounting / Business / Professionals

Industry/Entity Type

Accounting

Colors
ec1f27

Requirements
Nice to have
• Simple Clean design. Not to busy. Easy to modify the "wording text" in design
Should not have
• Too busy or too much color

```html
<!DOCTYPE html>
<html lang="en">
<head>
<meta charset="utf-8">
<title>Taxation Projection and Planning 2020 – Report Template</title>
<link href="https://fonts.googleapis.com/css2?family=Open+Sans:ital,wght@0,300;0,400;0,600;0,700;1,400;1,600;1,700&family=Arimo:ital,wght@0,400;0,700;1,700&family=Tinos:ital,wght@0,400;0,700;1,700&display=swap" rel="stylesheet">
<style>
:root{
  --brand-red:#b5121b;
  --ink:#2b2b2b;
  --body:#333333;
  --muted:#7a7a7a;
  --slate:#6d6e71;
  --mist:#f3f3f3;
  --backdrop:#1c1c1c;
  --paper:#ffffff;
  --row-a:#f6e3dc;
  --row-b:#fbf1ec;
  --quote-bg:#f6e6e8;
}
*{box-sizing:border-box;margin:0;padding:0}
html,body{width:1200px;height:1200px;overflow:hidden;background:var(--backdrop)}
.canvas{position:relative;width:1200px;height:1200px;background:var(--backdrop)}
.page{position:absolute;width:540px;height:765px;background:var(--paper);transform:scale(0.6211);transform-origin:0 0;overflow:hidden;font-family:Arimo,Arial,sans-serif;color:var(--body)}
.p1{left:67px;top:101px}.p2{left:435px;top:101px}.p3{left:797px;top:101px}
.p4{left:67px;top:624px}.p5{left:435px;top:624px}

.brand{position:absolute;left:51px;top:27px;line-height:1}
.brand-name{font-family:"Open Sans",sans-serif;font-weight:400;color:var(--brand-red);font-size:18px;letter-spacing:.5px}
.brand-sub{font-family:"Open Sans",sans-serif;font-size:5px;color:var(--muted);letter-spacing:.3px;margin-top:3px}

.cover{background:linear-gradient(150deg,var(--mist) 0%,var(--paper) 40%)}
.cover .brand{top:48px}
.cover .brand-name{font-size:29px}
.cover .brand-sub{font-size:8px;margin-top:4px}
.seal{position:absolute;left:425px;top:30px;width:88px;height:88px;border-radius:50%;background:radial-gradient(circle at 40% 35%,#d02a35,#8e0f17)}
.cover-art{position:absolute;left:0;top:500px;width:540px;height:265px;background:linear-gradient(160deg,var(--brand-red) 0%,#8f2a30 45%,var(--slate) 100%)}
.cover-title{position:absolute;left:142px;top:230px;font-family:"Open Sans",sans-serif;line-height:1}
.cover-title .kicker{color:var(--brand-red);font-weight:700;font-size:33px;display:block;margin-bottom:4px}
.cover-title .main{color:var(--ink);font-weight:300;font-size:49px;display:block;line-height:48px}
.client{position:absolute;left:142px;top:445px;font-family:"Open Sans",sans-serif;font-weight:600;font-size:14px;color:var(--ink)}
.web{position:absolute;right:50px;bottom:28px;font-family:"Open Sans",sans-serif;font-weight:700;font-size:11px;color:#fff}

.corner{position:absolute;left:484px;top:712px;width:56px;height:53px;background:var(--brand-red)}
.footer-copy{position:absolute;left:51px;top:726px;font-family:"Open Sans",sans-serif;font-size:7.7px;color:var(--body)}
.footer-ref{position:absolute;right:84px;top:726px;font-family:"Open Sans",sans-serif;font-size:7.7px;color:var(--brand-red)}
.footer-ref b{font-weight:700}
.page-no{position:absolute;left:497px;top:725px;font-family:"Open Sans",sans-serif;font-weight:700;font-size:9px;color:#fff}

.body-text{font-size:9.3px;line-height:1.22;color:var(--body)}
.body-text p{margin-bottom:10px}

.disclaimer{position:absolute;left:51px;top:165px;width:435px}
.disclaimer h1{text-align:center;font-size:17px;font-weight:700;color:var(--ink);margin-bottom:24px}
.disclaimer h2{font-size:9.3px;font-weight:700;color:var(--ink)}
.signoff{position:absolute;left:51px;top:530px;font-size:9.3px;line-height:1.3}
.signoff b{color:var(--ink)}

.purpose{position:absolute;left:51px;top:88px;width:440px}
.h-section{font-family:"Open Sans",sans-serif;font-weight:600;color:var(--ink);font-size:19px;margin-bottom:4px}
.h-sub{font-family:Arimo,Arial,sans-serif;font-style:italic;font-weight:700;font-size:14px;color:var(--ink);margin-bottom:10px}
.h-minor{font-family:Arimo,Arial,sans-serif;font-weight:700;font-size:13.5px;color:var(--ink);margin:14px 0 6px}
.bullets{list-style:disc;padding-left:14px;margin-top:-8px}
.bullets li{margin-bottom:3px}
.basis{width:228px}
.quote{position:absolute;left:292px;top:452px;width:220px;height:140px}
.quote-text{position:absolute;left:22px;top:24px;font-family:Tinos,serif;font-style:italic;font-weight:700;font-size:27px;line-height:30px;color:var(--brand-red);white-space:nowrap}

.sheet-label{position:absolute;left:51px;top:82px;font-style:italic;font-weight:700;font-size:14.5px;color:var(--ink)}
.sheet-head{position:absolute;left:51px;top:106px;width:438px;height:28px;background:#c8c9cb}
.sheet-row{position:absolute;left:51px;top:134px;width:438px;height:15px;background:#ececec}

.strategies{position:absolute;left:51px;top:85px;width:438px}
.strat-title{font-family:"Open Sans",sans-serif;font-style:italic;font-weight:700;font-size:18px;line-height:22px;color:var(--brand-red)}
.strat-sub{font-family:"Open Sans",sans-serif;font-style:italic;font-size:18px;color:var(--ink);margin:10px 0 16px}
.serif{font-family:Tinos,serif;color:var(--ink)}
.serif-h{font-size:14px;line-height:16px}
.serif-s{font-size:8px;margin-bottom:26px}
.serif-l{font-size:8px;margin:8px 0 8px}
.strat-table{width:438px;font-family:Tinos,serif;font-size:8px;line-height:1.28;color:var(--body)}
.strat-row{padding:6px 9px 8px}
.strat-row:nth-child(odd){background:var(--row-a)}
.strat-row:nth-child(even){background:var(--row-b)}
.strat-row h3{font-weight:700;font-size:8px;color:var(--ink);margin-bottom:9px}
.strat-row p{margin-bottom:9px}
.indent{padding-left:30px}
</style>
</head>
<body>
<div class="canvas">

  <!-- Cover -->
  <section class="page p1 cover">
    <div class="brand"><div class="brand-name">HARLOW REID</div><div class="brand-sub">CHARTERED ACCOUNTANTS</div></div>
    <div class="seal" role="img" aria-label="Red wax seal emblem"></div>
    <h1 class="cover-title"><span class="kicker">TAXATION</span><span class="main">PROJECTION<br>AND PLANNING<br>2020</span></h1>
    <div class="client">Client Name</div>
    <div class="cover-art" role="img" aria-label="Red and grey decorative band graphic"></div>
    <div class="web">www.harlowreid.com.au</div>
  </section>

  <!-- Disclaimer -->
  <section class="page p2">
    <div class="brand"><div class="brand-name">HARLOW REID</div><div class="brand-sub">CHARTERED ACCOUNTANTS</div></div>
    <div class="disclaimer body-text">
      <h1>DISCLAIMER</h1>
      <p>The taxation estimate has been prepared on the basis of information provided by the client. The report Is intended for internal tax planning purposes and represents a "What if scenario". It does not necessarily represent real or intended transactions.</p>
      <p>HarlowReid have not performed any tests to verify or validate any of the information provided by the client and accordingly express no assurance as to the outcome indicated.</p>
      <p>To the extent permitted by law we do not accept liability for any loss or damage which any person, other than the client may suffer arising from any negligence on our part. No person should rely on the Taxation estimate without having a full review or audit conducted on the data.</p>
      <h2>Superannuation</h2>
      <p>Provision of Advice is guided by legislative requirements to be provided in a Statement of Advice. Any and all comments regarding Superannuation are not to be taken as advice rather than statement of factual information about the situation. The statement is not a recommendation to take any action unless that action is required by law. The clients personal situation has not been considered in</p>
      <p>providing the information. Any action to be taken in relation to the information provided, should take into account the clients personal situation and consideration must be given as to whether action will be appropriate for the clients' objectives and needs. Specific Contribution amounts and SMSF product advice can only be provided under a Statement of Advice by a AFSL Holder.</p>
    </div>
    <div class="signoff"><b>HarlowReid</b><br>Chartered Accountants</div>
    <div class="footer-copy">© 2020 HarlowReid Chartered Accountants</div>
    <div class="footer-ref">2020 Tax Planning | <b>Client Name Here</b></div>
    <div class="corner" role="img" aria-label="Red corner accent"></div>
    <div class="page-no">2</div>
  </section>

  <!-- Purpose -->
  <section class="page p3">
    <svg style="position:absolute;left:0;top:0" width="540" height="765" viewBox="0 0 540 765">
      <polygon points="309,462 510,462 490,585 292,585" fill="var(--quote-bg)"/>
      <line x1="355" y1="462" x2="490" y2="462" stroke="var(--brand-red)" stroke-width="1.5"/>
      <line x1="312" y1="585" x2="460" y2="585" stroke="var(--brand-red)" stroke-width="1.5"/>
      <text x="318" y="478" font-family="Tinos,serif" font-weight="700" font-size="40" fill="var(--brand-red)">“</text>
      <text x="462" y="610" font-family="Tinos,serif" font-weight="700" font-size="40" fill="var(--brand-red)">”</text>
    </svg>
    <div class="brand"><div class="brand-name">HARLOW REID</div><div class="brand-sub">CHARTERED ACCOUNTANTS</div></div>
    <div class="purpose body-text">
      <h2 class="h-section">Purpose of Tax Planning</h2>
      <div class="h-sub">Why bother…..???</div>
      <p>Tax planning is the activities taken to minimise tax liabilities to ensure all available allowances, deductions, exclusions and exemptions are working together in the most tax effective manner to reduce the total tax bill.</p>
      <p>The purpose of this report is to provide a recommedation of strategies for you to consider for the year to come.&nbsp; This report is not intended to be our final advice to you, but instead a stating point in educating you on potential opportunities.</p>
      <p style="margin-top:22px">Tax planning strategies are typically employed to help a business achieve their financial and business goals. The benefits of tax planning are:</p>
      <ul class="bullets">
        <li>Lowering the Amount of taxable income</li>
        <li>Reducing the tax rate</li>
        <li>Allowing greater Control of when taxes get paid</li>
        <li>Better Management of your cashflow</li>
        <li>Eliminating nasty tax surprises</li>
      </ul>
      <h3 class="h-minor">Recomendations</h3>
      <p>We will provide you with a list of Action plans and a further list of &nbsp;……… The list will be broken down in Short term and Longer Term action.&nbsp; Also list of actions to follow up on …..work on this bit ……sjc</p>
      <h3 class="h-minor">Basis of Preparation</h3>
      <div class="basis">
        <p>The taxation estimate has been prepared on the basis of information provided by the client. The report is intended for internal tax planning purposes and represents a "What if scenario". It does not necessarily represent real or intended transactions.</p>
        <p>HarlowReid have not performed any tests to verify or validate any of the information provided by the client and accordingly express no assurance as to the outcome indicated.</p>
        <p>To the extent permitted by law we do not accept liability for any loss or damage which any person, other than the client may suffer arising from any negligence on our part. No person should rely on the Taxation estimate without having a full review or audit conducted on the data.</p>
      </div>
    </div>
    <div class="quote"><div class="quote-text">If you fail<br>to plan, you are<br>planning to fail</div></div>
    <div class="footer-copy">© 2020 HarlowReid Chartered Accountants</div>
    <div class="footer-ref">2020 Tax Planning | <b>Client Name Here</b></div>
    <div class="corner" role="img" aria-label="Red corner accent"></div>
    <div class="page-no">3</div>
  </section>

  <!-- Spreadsheet insert -->
  <section class="page p4">
    <div class="brand"><div class="brand-name">HARLOW REID</div><div class="brand-sub">CHARTERED ACCOUNTANTS</div></div>
    <div class="sheet-label">Excel sheets added here</div>
    <div class="sheet-head"></div>
    <div class="sheet-row"></div>
    <div class="footer-copy">© 2020 HarlowReid Chartered Accountants</div>
    <div class="footer-ref">2020 Tax Planning | <b>Client Name Here</b></div>
    <div class="corner" role="img" aria-label="Red corner accent"></div>
    <div class="page-no">4</div>
  </section>

  <!-- Strategies -->
  <section class="page p5">
    <div class="brand"><div class="brand-name">HARLOW REID</div><div class="brand-sub">CHARTERED ACCOUNTANTS</div></div>
    <div class="strategies">
      <h1 class="strat-title">Taxation Planning Stratagies<br>Main Taxation Plannings Strategies</h1>
      <div class="strat-sub">Stategy</div>
      <div class="serif serif-h">TAX PLANNING STRATEGIES</div>
      <div class="serif serif-s">A more detailed list of potential tax planning strategies is as follows:</div>
      <div class="serif serif-h">MAIN TAX PLANNING STRATEGIES</div>
      <div class="serif serif-l">STRATEGY</div>
      <div class="strat-table">
        <div class="strat-row">
          <h3>Bring Forward Expenses</h3>
          <p>If possible, you should incur any business use expenses prior to 30 JuneT his way that expense will be included in the current tax year rather than NEXT tax year, reducing your tax payable in this financial year.</p>
          <p>Examples include: consumables, repairs, computer and office supplies.</p>
        </div>
        <div class="strat-row">
          <h3>Defer Income</h3>
          <p>If possible, you should defer issuing invoices in the last week or two until after 30 June 2019. This way that income will be included in the 2020 tax year rather than the 2019 tax year, deferring tax on the income for a year. Cash basis taxpayers should defer receipt of payment if possible.</p>
        </div>
        <div class="strat-row">
          <h3>Accounts Receivable</h3>
          <p>Under the small business tax concessions, the financial statements can be prepared on a cash basis so amounts receivable can be removed from the financial statements for tax purposes</p>
        </div>
        <div class="strat-row">
          <h3>Accounts Payable</h3>
          <p>Under the small business tax concessions, the financial statements can be prepared on a cash basis so amounts payable can be removed from the financial statements for tax purposes<br>Depreciation From Purchased Assets that Cost more than $30,000</p>
          <p>A small business entity that purchases depreciating assets that cost more than:<br>
          <span class="indent">-&nbsp;&nbsp;&nbsp;&nbsp; $30,000 from 3 April 2019 - 30 June 2019</span><br>
          <span class="indent">-&nbsp;&nbsp;&nbsp;&nbsp; $25,000 from 29 January 2019 – 2 April 2019</span><br>
          <span class="indent">-&nbsp;&nbsp;&nbsp;&nbsp; $20,000 from 1 July 2018 – 28 January 2019</span></p>
          <p>Will receive the following tax deductions from pooling the asset(s) in a small business asset pool:<br>
          <span class="indent">□&nbsp;&nbsp;&nbsp; A 15% deduction in the 2019 tax year, regardless of when you purchased or acquired the asset during the year; and</span><br>
          <span class="indent">□&nbsp;&nbsp;&nbsp; A 30% deduction each year after the first year.</span></p>
        </div>
      </div>
    </div>
    <div class="footer-copy">© 2020 HarlowReid Chartered Accountants</div>
    <div class="footer-ref">2020 Tax Planning | <b>Client Name Here</b></div>
    <div class="corner" role="img" aria-label="Red corner accent"></div>
    <div class="page-no">5</div>
  </section>

</div>
</body>
</html>
```